Baby Shower Invitation for Vectored Image Provided

Corinne & Dorian's Baby Shower - Black/White/Gold Colors preferred
Please use the vectored portrait image attached. I'd like us on the lower right side of the invitation.
Can be horizontal or vertical layout.
The second image attached has the information needed for you to complete.
I don't want that style copied, it is just an example.

```html
<!DOCTYPE html>
<html lang="en">
<head>
<meta charset="utf-8">
<title>Corinne's Baby Shower Invitation</title>
<link href="https://fonts.googleapis.com/css2?family=Crimson+Pro:wght@400;500&family=Yellowtail&display=swap" rel="stylesheet">
<style>
  :root {
    --bg-top: #2a2a2a;
    --bg-bottom: #3b3b3b;
    --gold: #f3d54e;
    --pale-gold: #e9de8a;
    --white: #ffffff;
    --rule: #9a9a9a;
    --hatch-gold: #6e6734;
    --hatch-grey: #5c5c5c;
  }
  html, body { margin: 0; padding: 0; overflow: hidden; background: var(--bg-top); }
  .invitation {
    position: relative;
    width: 857px;
    height: 1200px;
    overflow: hidden;
    background: linear-gradient(180deg, var(--bg-top), var(--bg-bottom));
    color: var(--white);
    font-family: "Crimson Pro", Georgia, serif;
  }
  .decor { position: absolute; inset: 0; }
  .line-text, .script {
    position: absolute;
    left: 0; right: 0;
    margin: 0;
    text-align: center;
    white-space: nowrap;
  }
  .caps { font-size: 21px; letter-spacing: 5px; text-transform: uppercase; }
  .script { font-family: "Yellowtail", cursive; color: var(--gold); font-weight: 400; }
  .lead { font-size: 24px; letter-spacing: 1px; }
  .detail { font-size: 28px; letter-spacing: 0.5px; }
  .rule { position: absolute; height: 3px; background: var(--rule); }
  .side-col { position: absolute; left: 136px; width: 300px; text-align: center; font-size: 26px; line-height: 48px; }
  .side-col p { margin: 0; }
  .portrait {
    position: absolute;
    left: 518px; top: 752px;
    width: 300px; height: 448px;
    border-radius: 140px 140px 0 0;
    background: linear-gradient(180deg, #4a4a4a, #1d1d1d);
  }
</style>
</head>
<body>
<main class="invitation">
  <svg class="decor" width="857" height="1200" viewBox="0 0 857 1200" aria-hidden="true">
    <circle cx="36" cy="205" r="134" fill="var(--hatch-gold)"/>
    <circle cx="0" cy="304" r="50" fill="var(--white)"/>
    <circle cx="840" cy="250" r="125" fill="var(--hatch-grey)"/>
    <circle cx="780" cy="375" r="36" fill="var(--pale-gold)"/>
    <circle cx="679" cy="71" r="7" fill="var(--white)"/>
    <circle cx="754" cy="554" r="9" fill="var(--white)"/>
    <circle cx="139" cy="621" r="11" fill="var(--white)"/>
    <circle cx="71" cy="839" r="71" fill="var(--hatch-grey)"/>
    <circle cx="0" cy="795" r="54" fill="var(--pale-gold)"/>
    <circle cx="839" cy="857" r="80" fill="var(--white)"/>
    <circle cx="54" cy="1157" r="11" fill="var(--white)"/>
    <g stroke="var(--white)" stroke-width="3" stroke-linecap="round">
      <line x1="273" y1="38" x2="273" y2="88"/>
      <line x1="248" y1="63" x2="298" y2="63"/>
      <line x1="255" y1="45" x2="291" y2="81"/>
      <line x1="291" y1="45" x2="255" y2="81"/>
    </g>
    <g stroke="var(--gold)" stroke-width="4" stroke-linecap="round">
      <line x1="800" y1="55" x2="800" y2="153"/>
      <line x1="751" y1="104" x2="849" y2="104"/>
      <line x1="766" y1="70" x2="834" y2="138"/>
      <line x1="834" y1="70" x2="766" y2="138"/>
    </g>
    <g stroke="var(--gold)" stroke-width="4" stroke-linecap="round">
      <line x1="57" y1="857" x2="57" y2="957"/>
      <line x1="7" y1="907" x2="107" y2="907"/>
      <line x1="22" y1="872" x2="92" y2="942"/>
      <line x1="92" y1="872" x2="22" y2="942"/>
    </g>
  </svg>

  <p class="line-text caps" style="top:122px;">Twinkle, Twinkle</p>
  <h2 class="script" style="top:180px; font-size:68px; line-height:90px;">little boy</h2>
  <p class="line-text caps" style="top:298px;">Do you know how loved you are?</p>
  <div class="rule" style="left:348px; width:161px; top:361px;"></div>
  <p class="line-text lead" style="top:392px;">Please join us for a baby shower honoring</p>
  <h1 class="script" style="top:440px; font-size:78px; line-height:100px;">Corinne Ashworth</h1>
  <p class="line-text detail" style="top:598px;">Saturday, September 1st, 11:30am-2:30pm</p>
  <p class="line-text detail" style="top:655px;">The Willowmere 1487 Carden St. Raleigh, NC</p>

  <div class="rule" style="left:179px; width:209px; top:748px;"></div>
  <div class="side-col" style="top:772px;">
    <p>RSVP to Dorian at</p>
    <p>919-555-0148 by August 20th</p>
  </div>
  <div class="rule" style="left:179px; width:209px; top:904px;"></div>
  <div class="side-col" style="top:932px;">
    <p>Corinne is registered at</p>
    <p>Little Nest Baby</p>
  </div>
  <p class="script" style="left:136px; right:auto; width:300px; top:1042px; font-size:56px; line-height:72px;">See You There!</p>

  <div class="portrait" role="img" aria-label="Vector portrait of the expecting couple standing together"></div>
</main>
</body>
</html>
```